(LUMO PEAK ADVISORY SERVICE) Credit Repair Service

We are committed to customer service, Credit Repair Service, Consumer Finance, Landlord Tenant, Traffic, Estate Planning, Collection, Family Law, Civil Litigation, and so much more.

Vento Crest Prime Payment plans starting at $200 per month

Consumer Finance, Landlord Tenant, Traffic, Estate Planning, Collection, Family Law, Civil Litigation, and so much more

Credit Services

Tandem Orivex $1,700

One-on-One consultations with a Certified KURT© Professional

Bureau Challenges

Creditor Interventions

Inquiry Assist

Score Analysis

Report Watch

Crediway® Alerts

Cease & Desist Letters

KURT® Rating Monitor

Identity Protection

Personal Finance Tools

Tandem Amber $1,400

Bureau Challenges

Creditor Interventions

Inquiry Assist

Score Analysis

Report Watch

Crediway® Alerts

Tandem Copper $,1150

Bureau Challenges

Creditor Interventions

Industry/Entity Type

Consulting

Coding

Coded - Design and coding required

Number of Pages Required

1 page

Colors
cee9f5
85cae6
ecf7fb

Requirements
Must have
• We are committed to customer service, Credit Repair Service, Consumer Finance, Landlord Tenant, Traffic, Estate Planning, Collection, Family Law, Civil Litigation, and so much more.
• Vento Crest Prime Payment plans starting at $200 per month
• Consumer Finance, Landlord Tenant, Traffic, Estate Planning, Collection, Family Law, Civil Litigation, and so much more
• Credit Services
• Tandem Orivex $1,700
• One-on-One consultations with a Certified KURT© Professional
• Bureau Challenges
• Creditor Interventions
• Inquiry Assist
• Score Analysis
• Report Watch
• Crediway® Alerts
• Cease & Desist Letters
• KURT® Rating Monitor
• Identity Protection
• Personal Finance Tools
• Tandem Amber $1,400
• Bureau Challenges
• Creditor Interventions
• Inquiry Assist
• Score Analysis
• Report Watch
• Crediway® Alerts
• Tandem Copper $,1150
• Bureau Challenges
• Creditor Interventions
• Pricing, services, about us, generic pictures, contact information,
• Contact information -( wilma82dun@postnest.example) 4712 SE 215 Avenue Miami FL 33190
Nice to have

```html
<!DOCTYPE html>
<html lang="en">
<head>
<meta charset="utf-8">
<title>Lumo Peak Advisory Service</title>
<link rel="stylesheet" href="https://fonts.googleapis.com/css2?family=Lato:wght@400;700;900&family=Roboto:wght@400;500;700&display=swap">
<style>
:root{
  --blue:#4ea9d9;
  --blue-dark:#3a97c9;
  --blue-light:#85cae6;
  --blue-pale:#cee9f5;
  --blue-mist:#ecf7fb;
  --amber:#e5533a;
  --amber-light:#ef7d61;
  --ink:#1d1d1d;
  --text:#5a5a5a;
  --line:#dcdcdc;
  --night:#141414;
  --white:#ffffff;
}
*{box-sizing:border-box;margin:0;padding:0}
html,body{width:1200px;height:3321px;overflow:hidden}
body{position:relative;background:var(--white);font-family:"Roboto",Arial,sans-serif;color:var(--text)}
.abs{position:absolute}
.center-text{left:0;width:1200px;text-align:center}

/* header */
.site-header{position:absolute;left:0;top:0;width:1200px;height:110px;background:var(--blue);z-index:3}
.brand{position:absolute;left:100px;top:24px;display:flex;align-items:center;gap:18px;color:var(--white);font-family:"Roboto",Arial,sans-serif;font-weight:500}
.brand-mark{width:58px;height:58px;border-radius:50%;background:var(--white);opacity:.95}
.brand-name{font-size:28px;line-height:32px;letter-spacing:1px}
.brand-sub{font-size:17px;line-height:24px}
.main-nav a{position:absolute;top:44px;color:var(--white);font-weight:700;font-size:15px;text-decoration:none;letter-spacing:.3px}
.search-icon{position:absolute;left:1083px;top:44px}

/* hero */
.hero{position:absolute;left:0;top:110px;width:1200px;height:680px}
.hero-photo{position:absolute;inset:0;background:linear-gradient(120deg,#6b6a66 0%,#b9b5a8 35%,#d9dcd2 55%,#8a8d7a 80%,#4e5448 100%)}
.hero-title{position:absolute;top:160px;font-family:"Lato",Arial,sans-serif;font-weight:900;font-size:84px;line-height:100px;color:var(--white);letter-spacing:2px;text-shadow:0 2px 6px rgba(0,0,0,.25)}
.hero-sub{position:absolute;top:257px;font-family:"Lato",Arial,sans-serif;font-weight:700;font-size:46px;line-height:56px;color:var(--white);letter-spacing:3px;text-shadow:0 2px 6px rgba(0,0,0,.25)}
.btn{display:flex;align-items:center;justify-content:center;gap:8px;background:var(--blue);color:var(--white);font-family:"Roboto",Arial,sans-serif;font-weight:700;font-size:16px;text-transform:uppercase;text-decoration:none}
.hero .btn{position:absolute;left:507px;top:344px;width:188px;height:46px}
.carousel-arrow{position:absolute;top:222px;width:44px;height:44px;border-radius:50%;background:rgba(40,40,40,.6)}

/* section headings */
.ghost{position:absolute;font-family:"Lato",Arial,sans-serif;font-weight:900;font-size:70px;line-height:80px;color:rgba(0,0,0,.06);letter-spacing:1px}
.section-title{position:absolute;font-family:"Lato",Arial,sans-serif;font-weight:900;font-size:36px;line-height:44px;color:var(--ink)}

/* services */
.services{position:absolute;left:0;top:760px;width:1200px;height:1000px;background:linear-gradient(180deg,#ffffff 0%,#f6f7f8 40%,#eef0f2 75%,#ffffff 100%)}
.services-intro{position:absolute;left:270px;top:168px;width:660px;text-align:center;font-size:14px;line-height:27px;color:var(--text)}
.service-card{position:absolute;width:306px;height:216px;background:rgba(255,255,255,.92);border:1px solid var(--line);text-align:center}
.service-card svg{position:absolute;left:113px;top:20px}
.service-card h3{position:absolute;left:0;top:106px;width:100%;font-family:"Roboto",Arial,sans-serif;font-weight:500;font-size:17px;line-height:26px;color:var(--ink);text-transform:uppercase}
.service-card p{position:absolute;left:30px;top:140px;width:246px;font-size:13.5px;line-height:24px;color:var(--text)}
.services .btn{position:absolute;left:467px;top:788px;width:233px;height:48px}

/* special offer */
.special{position:absolute;left:0;top:1716px;width:1200px;height:476px}
.special-label{position:absolute;top:96px;font-size:21px;line-height:30px;color:var(--white);font-weight:400;letter-spacing:.5px}
.offer-ribbon{position:absolute;left:270px;top:159px}
.offer-text{position:absolute;top:175px;font-weight:700;font-size:24px;line-height:30px;color:var(--white)}
.special-copy{position:absolute;left:300px;top:254px;width:600px;text-align:center;font-size:13px;line-height:26px;color:#e6e6e6}
.btn-outline{position:absolute;left:516px;top:336px;width:170px;height:42px;border:2px solid var(--white);color:var(--white);font-weight:500;font-size:16px;display:flex;align-items:center;justify-content:center;text-transform:uppercase}

/* packages */
.package{position:absolute;top:2402px;width:308px;height:450px;background:var(--white);box-shadow:0 0 8px rgba(0,0,0,.15)}
.package-ribbon{position:absolute;left:20px;top:-20px}
.package-name{position:absolute;left:20px;top:-20px;width:268px;height:52px;line-height:52px;text-align:center;color:var(--white);font-weight:500;font-size:18px;text-transform:uppercase}
.package-price{position:absolute;left:0;top:88px;width:100%;text-align:center;font-weight:700;font-size:30px;line-height:40px;color:var(--blue-dark)}
.package-list{position:absolute;left:76px;top:143px;list-style:none;font-size:13.5px;line-height:22px;color:var(--text)}
.package-list li::before{content:"»";color:var(--blue);margin-right:12px;font-weight:700}
.package .btn{position:absolute;left:89px;top:385px;width:130px;height:36px;font-size:13px;font-weight:500}
.package.featured .package-price{color:var(--amber)}
.package.featured .package-list li::before{color:var(--amber)}
.package.featured .btn{background:var(--amber)}

/* footer */
.footer-shape{position:absolute;left:0;top:2925px}
.footer-col h4{position:absolute;top:3058px;color:var(--white);font-weight:700;font-size:16px;line-height:22px}
.contact-line{position:absolute;left:100px;display:flex;align-items:center;gap:14px;font-size:13px;color:#d9d9d9}
.social{position:absolute;top:3103px;width:34px;height:34px;border-radius:50%;background:var(--white)}
.email-field{position:absolute;left:801px;top:3104px;width:299px;height:40px;border:1px solid var(--white);color:#e0e0e0;font-size:14px;line-height:38px;padding-left:14px}
.email-field svg{position:absolute;right:12px;top:13px}
.footer-subscribe{position:absolute;left:801px;top:3155px;width:110px;height:36px;font-size:13px;font-weight:500}
.footer-rule{position:absolute;left:100px;top:3226px;width:1000px;height:1px;background:#3d3d3d}
.copyright{position:absolute;top:3268px;font-size:13px;line-height:18px;color:#d9d9d9}
</style>
</head>
<body>

<header class="site-header">
  <div class="brand">
    <span class="brand-mark"></span>
    <div>
      <div class="brand-name">LUMO PEAK</div>
      <div class="brand-sub">Advisory Service</div>
    </div>
  </div>
  <nav class="main-nav">
    <a href="#" style="left:571px">HOME</a>
    <a href="#" style="left:651px">PRICING</a>
    <a href="#" style="left:746px">SERVICES</a>
    <a href="#" style="left:852px">ABOUT US</a>
    <a href="#" style="left:958px">CONTACT US</a>
  </nav>
  <svg class="search-icon" width="18" height="18" viewBox="0 0 18 18"><circle cx="7.5" cy="7.5" r="5.5" fill="none" stroke="#fff" stroke-width="2.4"/><line x1="11.5" y1="11.5" x2="16" y2="16" stroke="#fff" stroke-width="2.6" stroke-linecap="round"/></svg>
</header>

<section class="hero">
  <div class="hero-photo" role="img" aria-label="Photo of three business people meeting around a desk with a laptop"></div>
  <span class="carousel-arrow" style="left:16px"><svg width="44" height="44" viewBox="0 0 44 44"><polyline points="25,15 18,22 25,29" fill="none" stroke="#fff" stroke-width="3"/></svg></span>
  <span class="carousel-arrow" style="left:1140px"><svg width="44" height="44" viewBox="0 0 44 44"><polyline points="19,15 26,22 19,29" fill="none" stroke="#fff" stroke-width="3"/></svg></span>
  <h1 class="hero-title center-text">LUMO PEAK</h1>
  <p class="hero-sub center-text">ADVISORY SERVICE</p>
  <a href="#" class="btn">Get Started
    <svg width="16" height="16" viewBox="0 0 16 16"><circle cx="8" cy="8" r="8" fill="#fff"/><polyline points="6.5,4.5 10,8 6.5,11.5" fill="none" stroke="#4ea9d9" stroke-width="2"/></svg>
  </a>
  <svg class="abs" style="left:0;top:0" width="1200" height="680" viewBox="0 0 1200 680">
    <polygon points="0,543 600,655 1200,550 1200,680 0,680" fill="#fff"/>
    <polyline points="0,543 600,655 1200,550" fill="none" stroke="#4ea9d9" stroke-width="6"/>
    <polyline points="585,582 600,596 615,582" fill="none" stroke="#fff" stroke-width="4"/>
    <polyline points="585,594 600,608 615,594" fill="none" stroke="#fff" stroke-width="4"/>
  </svg>
</section>

<section class="services">
  <div class="ghost center-text" style="top:86px">OUR SERVICES</div>
  <h2 class="section-title center-text" style="top:104px">OUR SERVICES</h2>
  <p class="services-intro">At vero eos et accusamus et iusto odio dignissimos ducimus praesentium voluptatum deleniti atque corrupti quos dolores et quas molestias excepturi sint occaecati cupiditate non provident similique</p>

  <article class="service-card" style="left:100px;top:256px">
    <svg width="80" height="80" viewBox="0 0 80 80" fill="none" stroke="#3a97c9" stroke-width="3.5" stroke-linejoin="round"><rect x="6" y="20" width="56" height="38" rx="5"/><line x1="6" y1="32" x2="62" y2="32"/><polyline points="42,52 52,62 74,38"/></svg>
    <h3>Credit Repair Service</h3>
    <p>CFD's are a synthetic equity product, which mirror the economic benefits</p>
  </article>
  <article class="service-card" style="left:447px;top:256px">
    <svg width="80" height="80" viewBox="0 0 80 80" fill="#3a97c9"><rect x="10" y="52" width="10" height="20"/><rect x="24" y="44" width="10" height="28"/><rect x="38" y="36" width="10" height="36"/><rect x="52" y="28" width="10" height="44"/><polyline points="10,44 30,30 42,36 64,16" fill="none" stroke="#3a97c9" stroke-width="3.5"/><polygon points="58,12 70,10 68,22"/></svg>
    <h3>Consumer Finance</h3>
    <p>Norvane offers 24 hour trading coverage of all major pairs with services</p>
  </article>
  <article class="service-card" style="left:795px;top:256px">
    <svg width="80" height="80" viewBox="0 0 80 80" fill="none" stroke="#3a97c9" stroke-width="3.5" stroke-linejoin="round"><polyline points="20,40 40,20 60,40"/><rect x="26" y="38" width="28" height="22"/><rect x="36" y="46" width="8" height="14"/><path d="M8 64 H30 L40 70 H66 L72 62"/></svg>
    <h3>Landlord Tenant</h3>
    <p>A futures contract is a standardized agreement, made on a recognized</p>
  </article>
  <article class="service-card" style="left:100px;top:511px">
    <svg width="80" height="80" viewBox="0 0 80 80" fill="none" stroke="#3a97c9" stroke-width="3.5" stroke-linejoin="round"><polyline points="8,40 40,12 72,40"/><rect x="18" y="36" width="44" height="34"/><rect x="33" y="48" width="14" height="22"/></svg>
    <h3>Estate Planning</h3>
    <p>Norvane provides clients with 24-hour execution on global exchanges.</p>
  </article>
  <article class="service-card" style="left:447px;top:511px">
    <svg width="80" height="80" viewBox="0 0 80 80" fill="none" stroke="#3a97c9" stroke-width="3.5" stroke-linejoin="round"><polyline points="10,38 40,12 70,38"/><rect x="18" y="34" width="44" height="38"/><circle cx="40" cy="46" r="7" fill="#3a97c9"/><path d="M28 72 C28 60 52 60 52 72" fill="#3a97c9"/></svg>
    <h3>Family Law</h3>
    <p>A bond is a debt security, wherein an authorized issuer owes the holders</p>
  </article>
  <article class="service-card" style="left:795px;top:511px">
    <svg width="80" height="80" viewBox="0 0 80 80" fill="none" stroke="#3a97c9" stroke-width="3.5" stroke-linejoin="round"><polyline points="4,30 18,24 30,28"/><polyline points="76,30 62,24 48,28"/><path d="M30 28 L48 28 L60 46 L44 62 L24 46 Z" fill="#3a97c9"/><line x1="4" y1="30" x2="20" y2="50"/><line x1="76" y1="30" x2="62" y2="48"/></svg>
    <h3>Civil Litigation</h3>
    <p>Cryptocurrencies also known as digital currencies are fastest growing</p>
  </article>

  <a href="#" class="btn">View All Services
    <svg width="16" height="16" viewBox="0 0 16 16"><circle cx="8" cy="8" r="8" fill="#fff"/><polyline points="6.5,4.5 10,8 6.5,11.5" fill="none" stroke="#4ea9d9" stroke-width="2"/></svg>
  </a>
</section>

<section class="special">
  <svg class="abs" style="left:0;top:0" width="1200" height="476" viewBox="0 0 1200 476" role="img" aria-label="Dark photo of hands signing papers on a desk">
    <defs>
      <linearGradient id="specialShade" x1="0" y1="0" x2="1" y2="1">
        <stop offset="0" stop-color="#3b3f46"/>
        <stop offset=".5" stop-color="#24272c"/>
        <stop offset="1" stop-color="#111214"/>
      </linearGradient>
    </defs>
    <polygon points="0,88 600,0 1200,88 1200,387 600,476 0,387" fill="url(#specialShade)"/>
  </svg>
  <div class="special-label center-text">SPECIAL FOR YOU</div>
  <svg class="offer-ribbon" width="660" height="62" viewBox="0 0 660 62">
    <polygon points="0,8 30,8 30,58 0,58 14,33" fill="#2f86b6"/>
    <polygon points="660,8 630,8 630,58 660,58 646,33" fill="#2f86b6"/>
    <rect x="20" y="2" width="620" height="52" fill="#4ea9d9"/>
  </svg>
  <div class="offer-text center-text">Vento Crest Prime Payment plans starting at $200/ month</div>
  <p class="special-copy">Neque porro quisquam est, qui dolorem ipsum quia dolor sit amet, consectetur, adipisci velit, sed quia non numquam eius modi tempora incidunt ut labore et dolore</p>
  <a href="#" class="btn-outline">View More
    <svg style="margin-left:8px" width="16" height="16" viewBox="0 0 16 16"><circle cx="8" cy="8" r="8" fill="#fff"/><polyline points="6.5,4.5 10,8 6.5,11.5" fill="none" stroke="#222" stroke-width="2"/></svg>
  </a>
</section>

<div class="ghost center-text" style="top:2260px">SERVICE PACKAGES</div>
<h2 class="section-title center-text" style="top:2281px">SERVICE PACKAGES</h2>

<article class="package" style="left:100px">
  <svg class="package-ribbon" width="268" height="66" viewBox="0 0 268 66"><polygon points="0,0 268,0 268,66 134,52 0,66" fill="#85cae6"/><rect x="12" y="10" width="244" height="42" fill="#3a97c9"/></svg>
  <div class="package-name">Tandem Copper</div>
  <div class="package-price">$1,150</div>
  <ul class="package-list"><li>Bureau Challenges</li><li>Creditor Interventions</li></ul>
  <a href="#" class="btn">Get Started</a>
</article>

<article class="package featured" style="left:447px">
  <svg class="package-ribbon" width="268" height="66" viewBox="0 0 268 66"><polygon points="0,0 268,0 268,66 134,52 0,66" fill="#ef7d61"/><rect x="12" y="10" width="244" height="42" fill="#e5533a"/></svg>
  <div class="package-name">Tandem Amber</div>
  <div class="package-price">$1,400</div>
  <ul class="package-list"><li>Bureau Challenges</li><li>Creditor Interventions</li><li>Inquiry Assist</li><li>Score Analysis</li><li>Report Watch</li><li>Crediway® Alerts</li></ul>
  <a href="#" class="btn">Get Started</a>
</article>

<article class="package" style="left:795px">
  <svg class="package-ribbon" width="268" height="66" viewBox="0 0 268 66"><polygon points="0,0 268,0 268,66 134,52 0,66" fill="#85cae6"/><rect x="12" y="10" width="244" height="42" fill="#3a97c9"/></svg>
  <div class="package-name">Tandem Orivex</div>
  <div class="package-price">$1,700</div>
  <ul class="package-list"><li>Bureau Challenges</li><li>Creditor Interventions</li><li>Inquiry Assist</li><li>Score Analysis</li><li>Report Watch</li><li>Crediway® Alerts</li><li>Cease &amp; Desist Letters</li><li>KURT® Rating Monitor</li><li>Identity Protection</li><li>Personal Finance Tools</li></ul>
  <a href="#" class="btn">Get Started</a>
</article>

<footer>
  <svg class="footer-shape" width="1200" height="396" viewBox="0 0 1200 396">
    <polygon points="0,97 600,8 1200,97 1200,396 0,396" fill="#141414"/>
    <polyline points="0,97 600,8 1200,97" fill="none" stroke="#4ea9d9" stroke-width="6"/>
  </svg>
  <div class="footer-col"><h4 style="left:100px">Contact Us</h4></div>
  <div class="contact-line" style="top:3106px">
    <svg width="16" height="20" viewBox="0 0 16 20"><path d="M8 0 C3.6 0 0 3.4 0 7.6 C0 13 8 20 8 20 C8 20 16 13 16 7.6 C16 3.4 12.4 0 8 0 Z" fill="#fff"/><circle cx="8" cy="7.5" r="3" fill="#141414"/></svg>
    <span>4712 SE 215 Avenue Miami FL 33190</span>
  </div>
  <div class="contact-line" style="top:3151px">
    <svg width="16" height="12" viewBox="0 0 16 12"><rect width="16" height="12" rx="1" fill="#fff"/><polyline points="0,1 8,7 16,1" fill="none" stroke="#141414" stroke-width="1.5"/></svg>
    <span>wilma82dun@postnest.example</span>
  </div>

  <div class="footer-col"><h4 style="left:494px">Follow Us On</h4></div>
  <span class="social" style="left:490px"></span>
  <span class="social" style="left:534px"></span>
  <span class="social" style="left:579px"></span>
  <span class="social" style="left:623px"></span>

  <div class="footer-col"><h4 style="left:810px">Newsletter Subscribe</h4></div>
  <div class="email-field">Enter Email
    <svg width="16" height="12" viewBox="0 0 16 12"><rect width="16" height="12" rx="1" fill="#fff"/><polyline points="0,1 8,7 16,1" fill="none" stroke="#141414" stroke-width="1.5"/></svg>
  </div>
  <a href="#" class="btn footer-subscribe">Subscribe</a>

  <div class="footer-rule"></div>
  <p class="copyright center-text">© Copyright 2018 Lumo Peak Advisory Service. All Rights Reserved.</p>
</footer>

</body>
</html>
```